Engineering Consultant Business Card

I'm starting a new business as a high-end engineering consultant in a niche field. I've attached the jpg for my logo plus the branding guideline document that I've been following. You can see my business website here: www.tarvikworks.com
I'd like a business card that has the logo on one side, then the other side has (in any order): Tarvik Works, Inc.
Dana Whitlock
President and Chief EMC Engineer
www.tarvikworks.com
dana@tarvikworks.com
Optional: motto "We catch interference issues early, so your hardware passes compliance the first time."
I'm not planning on including a phone number
Target Market(s)
Businesses, especially makers of electronics hardware
Industry/Entity Type
Electrical engineering
Contact Information for Business Card
Company name, my name, website, email

```html
<!DOCTYPE html>
<html lang="en">
<head>
<meta charset="utf-8">
<title>Tarvik Works, Inc. — Business Card</title>
<link href="https://fonts.googleapis.com/css2?family=Open+Sans:wght@400;600;800&display=swap" rel="stylesheet">
<style>
  :root {
    --backdrop: #232323;
    --card: #151515;
    --card-back: #121212;
    --pattern: #1b1b1b;
    --brand-blue: #2f4aa8;
    --text-light: #f2f2f2;
    --shadow: rgba(0, 0, 0, 0.55);
  }
  * { box-sizing: border-box; margin: 0; padding: 0; }
  html, body {
    width: 1200px;
    height: 780px;
    overflow: hidden;
    background: var(--backdrop);
    font-family: "Open Sans", Arial, sans-serif;
  }
  .canvas {
    width: 1200px;
    height: 780px;
    display: flex;
    align-items: center;
    justify-content: center;
    gap: 40px;
  }
  .card {
    position: relative;
    width: 540px;
    height: 309px;
    border-radius: 22px;
    overflow: hidden;
    box-shadow: 0 18px 36px var(--shadow);
    border-bottom: 4px solid var(--brand-blue);
    border-left: 2px solid var(--brand-blue);
  }

  /* Back side */
  .card--back { background: var(--card-back); }
  .card__pattern {
    position: absolute;
    inset: 0;
    background: radial-gradient(ellipse at center, var(--pattern) 0%, var(--card-back) 80%);
  }
  .brand-mark {
    position: absolute;
    left: 50%;
    top: 50%;
    transform: translate(-50%, -50%);
    display: flex;
    align-items: center;
    gap: 10px;
    color: var(--brand-blue);
    font-weight: 800;
    font-size: 22px;
    white-space: nowrap;
  }
  .brand-mark__dot {
    width: 18px;
    height: 18px;
    border-radius: 50%;
    background: var(--brand-blue);
    flex: none;
  }

  /* Front side */
  .card--front { background: var(--card); }
  .front__brand {
    position: absolute;
    left: 26px;
    top: 114px;
    display: flex;
    align-items: center;
    gap: 8px;
    color: var(--brand-blue);
    font-weight: 800;
    font-size: 19px;
    white-space: nowrap;
  }
  .front__brand .brand-mark__dot { width: 16px; height: 16px; }
  .front__divider {
    position: absolute;
    left: 262px;
    top: 70px;
    width: 1px;
    height: 128px;
    background: var(--brand-blue);
  }
  .contact {
    position: absolute;
    left: 284px;
    top: 72px;
    color: var(--text-light);
  }
  .contact__name {
    color: var(--brand-blue);
    font-weight: 800;
    font-size: 24px;
    line-height: 1.1;
  }
  .contact__title {
    font-size: 13px;
    margin-top: 4px;
  }
  .contact__list {
    list-style: none;
    margin-top: 14px;
    font-size: 13.5px;
  }
  .contact__item {
    display: flex;
    align-items: center;
    gap: 8px;
    margin-top: 4px;
  }
  .contact__icon { width: 14px; height: 14px; flex: none; }
  .motto-band {
    position: absolute;
    left: 0;
    right: 0;
    bottom: 14px;
    height: 24px;
    background: var(--brand-blue);
    color: var(--text-light);
    font-size: 11.5px;
    display: flex;
    align-items: center;
    justify-content: center;
    white-space: nowrap;
  }
</style>
</head>
<body>
<main class="canvas">
  <section class="card card--back" aria-label="Card back">
    <div class="card__pattern" role="img" aria-label="Embossed repeating brand pattern in dark tones"></div>
    <div class="brand-mark">
      <span class="brand-mark__dot"></span>
      <span class="brand-mark__name">Tarvik Works, Inc.</span>
    </div>
  </section>

  <section class="card card--front" aria-label="Card front">
    <div class="front__brand">
      <span class="brand-mark__dot"></span>
      <span>Tarvik Works, Inc.</span>
    </div>
    <div class="front__divider"></div>
    <div class="contact">
      <h1 class="contact__name">Dana Whitlock</h1>
      <p class="contact__title">President and Chief EMC Engineer</p>
      <ul class="contact__list">
        <li class="contact__item">
          <svg class="contact__icon" viewBox="0 0 16 16" aria-hidden="true">
            <circle cx="8" cy="8" r="6.5" fill="none" stroke="#2f4aa8" stroke-width="1.6"/>
            <ellipse cx="8" cy="8" rx="2.8" ry="6.5" fill="none" stroke="#2f4aa8" stroke-width="1.2"/>
            <line x1="1.5" y1="8" x2="14.5" y2="8" stroke="#2f4aa8" stroke-width="1.2"/>
          </svg>
          <span>www.tarvikworks.com</span>
        </li>
        <li class="contact__item">
          <svg class="contact__icon" viewBox="0 0 16 16" aria-hidden="true">
            <rect x="1.5" y="3.5" width="13" height="9" fill="none" stroke="#2f4aa8" stroke-width="1.6"/>
            <polyline points="1.5,3.5 8,9 14.5,3.5" fill="none" stroke="#2f4aa8" stroke-width="1.4"/>
          </svg>
          <span>dana@tarvikworks.com</span>
        </li>
      </ul>
    </div>
    <p class="motto-band">We catch interference issues early, so your hardware passes compliance the first time.</p>
  </section>
</main>
</body>
</html>
```